Company Mission & Values Poster

I'd like an A2 Portrait Poster displaying our company's Mission & Values.
See our website for our logo, fonts, mission & values.
https://talvendo.com.au/

Our Mission: Creating homes for abundant life
Values: Love, Thinking, Team, Zoe.

Some ideas to consider:
Mission as the Headline then
A logo for each of the 4 Values and the words

Target Market(s)

Myself & my team

Industry/Entity Type

Real Estate

Font styles to use
Other font styles liked:
• Company fonts as seen on our website

```html
<!DOCTYPE html>
<html lang="en">
<head>
<meta charset="utf-8">
<title>Talvendo – Mission &amp; Values Poster</title>
<link href="https://fonts.googleapis.com/css2?family=Tinos&family=Poppins:wght@400;600;700;800&display=swap" rel="stylesheet">
<style>
  :root {
    --forest: #233b32;
    --sage: #a9c996;
    --paper: #ffffff;
    --backdrop: #efefec;
    --ink: #26302c;
  }
  * { margin: 0; padding: 0; box-sizing: border-box; }
  html, body { width: 1200px; height: 3141px; overflow: hidden; background: var(--backdrop); }
  .poster {
    position: absolute; left: 40px; top: 777px;
    width: 800px; height: 1133px;
    transform: scale(1.4); transform-origin: 0 0;
    background: var(--paper);
    box-shadow: 0 2px 6px rgba(0,0,0,.18);
    overflow: hidden;
    font-family: "Poppins", sans-serif;
    color: var(--ink);
  }
  .base-band { position: absolute; left: 0; right: 0; top: 567px; bottom: 0; background: var(--forest); }
  .values-card {
    position: absolute; left: 39px; top: 0; width: 721px; height: 790px;
    background: var(--paper); border-radius: 0 0 30px 30px;
  }
  .brand-name {
    position: absolute; left: 0; right: 0; top: 78px; text-align: center;
    font-family: "Tinos", serif; font-size: 66px; letter-spacing: 10px;
    color: var(--forest); line-height: 1;
  }
  .diagram { position: absolute; left: 0; top: 0; width: 800px; height: 800px; }
  .value { position: absolute; }
  .value h2 {
    font-family: "Tinos", serif; font-weight: 400; font-size: 35px;
    line-height: 1; color: var(--ink); margin-bottom: 6px;
  }
  .value p { font-size: 12.3px; line-height: 14.6px; color: var(--ink); }
  .value--love { left: 135px; top: 262px; width: 185px; }
  .value--thinking { left: 518px; top: 262px; width: 170px; }
  .value--team { left: 135px; top: 522px; width: 205px; }
  .value--team p, .value--zoe p { font-size: 13.4px; line-height: 16.1px; }
  .value--zoe { left: 518px; top: 522px; width: 170px; }
  .values-label {
    position: absolute; left: 300px; width: 200px; top: 470px; text-align: center;
    font-weight: 800; font-size: 31px; line-height: 31px; color: var(--ink);
  }
  .mission { position: absolute; left: 130px; top: 820px; width: 600px; color: var(--paper); }
  .mission-heading {
    position: absolute; left: 88px; top: 14px;
    font-weight: 800; font-size: 52px; line-height: 1; letter-spacing: 1px; white-space: nowrap;
  }
  .mission-heading .accent { color: var(--sage); }
  .mission-icon { position: absolute; left: -1px; top: 0; width: 76px; height: 76px; }
  .mission-statement {
    position: absolute; left: 0; top: 86px;
    font-family: "Tinos", serif; font-size: 41px; line-height: 1; white-space: nowrap;
  }
  .mission-belief {
    position: absolute; left: 0; top: 140px; width: 540px;
    font-size: 13.6px; line-height: 17.5px;
  }
  .mission-belief strong { color: var(--sage); font-weight: 700; }
</style>
</head>
<body>
<main class="poster">
  <div class="base-band"></div>
  <div class="values-card"></div>

  <h1 class="brand-name">TALVENDO</h1>

  <svg class="diagram" viewBox="0 0 800 800" aria-hidden="true">
    <g fill="none" stroke-width="5" stroke-linecap="round">
      <!-- love frame -->
      <path d="M317 243 H128 Q100 243 100 271 V437 Q100 465 128 465 H295" stroke="var(--sage)"/>
      <path d="M378 297 V372" stroke="var(--sage)"/>
      <!-- thinking frame -->
      <path d="M486 246 H668 Q696 246 696 274 V437 Q696 465 668 465 H503" stroke="var(--forest)"/>
      <path d="M420 297 V372" stroke="var(--forest)"/>
      <!-- team frame -->
      <path d="M317 726 H128 Q100 726 100 698 V533 Q100 505 128 505 H295" stroke="var(--forest)"/>
      <path d="M378 664 V588" stroke="var(--forest)"/>
      <!-- zoe frame -->
      <path d="M486 726 H668 Q696 726 696 698 V533 Q696 505 668 505 H503" stroke="var(--sage)"/>
      <path d="M420 664 V588" stroke="var(--sage)"/>
    </g>
    <!-- central hub -->
    <circle cx="400" cy="485" r="108" fill="var(--paper)" stroke="var(--forest)" stroke-width="5"/>
    <circle cx="400" cy="485" r="96" fill="var(--paper)" stroke="var(--sage)" stroke-width="5"/>
    <g transform="translate(400 425)" fill="var(--forest)">
      <path d="M0 10 C-14 -1 -12 -15 0 -8 C12 -15 14 -1 0 10Z"/>
      <path d="M-20 -6 V10 Q-20 20 -8 24 V30 H-2 V18 Q-14 14 -14 4 V-6Z"/>
      <path d="M20 -6 V10 Q20 20 8 24 V30 H2 V18 Q14 14 14 4 V-6Z"/>
    </g>

    <!-- love icon -->
    <circle cx="355" cy="259" r="36" fill="var(--paper)" stroke="var(--sage)" stroke-width="5"/>
    <g fill="var(--forest)">
      <path d="M347 262 C330 250 334 236 346 242 C356 236 362 250 347 262Z"/>
      <path d="M360 280 C340 266 344 249 359 256 C372 249 378 266 360 280Z"/>
      <circle cx="372" cy="244" r="2"/><circle cx="340" cy="276" r="2"/>
    </g>
    <!-- thinking icon -->
    <circle cx="448" cy="259" r="36" fill="var(--paper)" stroke="var(--forest)" stroke-width="5"/>
    <g fill="var(--forest)">
      <circle cx="448" cy="253" r="11"/>
      <rect x="442" y="265" width="12" height="5" rx="1"/>
      <rect x="443" y="272" width="10" height="4" rx="1"/>
      <g stroke="var(--forest)" stroke-width="2.5" stroke-linecap="round">
        <path d="M448 234 V237M431 253 H434M462 253 H465M436 241 L438 243M460 241 L458 243"/>
      </g>
    </g>
    <!-- team icon -->
    <circle cx="355" cy="702" r="36" fill="var(--paper)" stroke="var(--forest)" stroke-width="5"/>
    <g fill="var(--forest)">
      <circle cx="355" cy="690" r="8"/>
      <path d="M341 716 Q341 700 355 700 Q369 700 369 716Z"/>
      <circle cx="337" cy="696" r="6"/>
      <path d="M326 716 Q326 704 337 704 Q343 704 345 708 Q339 710 339 716Z"/>
      <circle cx="373" cy="696" r="6"/>
      <path d="M384 716 Q384 704 373 704 Q367 704 365 708 Q371 710 371 716Z"/>
    </g>
    <!-- zoe icon -->
    <circle cx="448" cy="702" r="36" fill="var(--paper)" stroke="var(--sage)" stroke-width="5"/>
    <g transform="translate(448 696)" fill="var(--forest)">
      <path d="M0 8 C-12 -1 -10 -13 0 -7 C10 -13 12 -1 0 8Z"/>
      <path d="M-17 -6 V8 Q-17 17 -7 20 V25 H-2 V15 Q-12 12 -12 4 V-6Z"/>
      <path d="M17 -6 V8 Q17 17 7 20 V25 H2 V15 Q12 12 12 4 V-6Z"/>
    </g>
  </svg>

  <section class="value value--love">
    <h2>Love</h2>
    <p>Our mission is founded in our love and respect for people – those we develop for, those in our teams and those in the communities we create and operate within.</p>
  </section>
  <section class="value value--thinking">
    <h2>Thinking</h2>
    <p>We believe in the power of thinking. Our rigorous and creative processes create beautifully considered solutions for our purchasers, the communities we develop within and the environment.</p>
  </section>
  <section class="value value--team">
    <h2>Team</h2>
    <p>Property development is a team sport. We surround ourselves with the best designers and advisers. We strive to create an environment that allows them to do their best work and love doing it.</p>
  </section>
  <section class="value value--zoe">
    <h2>Zoe</h2>
    <p>Our mission is to create places for ‘Zoe’ – the Greek word for abundant life. We do this through exquisite design, quality construction and celebrating nature.</p>
  </section>
  <div class="values-label">OUR<br>VALUES</div>

  <section class="mission">
    <svg class="mission-icon" viewBox="0 0 76 76" aria-hidden="true">
      <circle cx="36" cy="40" r="34" fill="var(--sage)"/>
      <circle cx="36" cy="40" r="24" fill="var(--forest)"/>
      <circle cx="36" cy="40" r="16" fill="var(--sage)"/>
      <circle cx="36" cy="40" r="7" fill="var(--forest)"/>
      <path d="M36 40 L64 12" stroke="var(--forest)" stroke-width="7"/>
      <path d="M36 40 L64 12" stroke="var(--sage)" stroke-width="3"/>
      <path d="M58 10 L66 2 L68 10 L60 18Z" fill="var(--sage)"/>
    </svg>
    <h2 class="mission-heading">OUR <span class="accent">MISSION</span></h2>
    <p class="mission-statement">Creating homes for abundant life.</p>
    <p class="mission-belief"><strong>We wholeheartedly believe that home is an extraordinary place:</strong><br>a haven where life unfolds in all its glory. Where we find solace, make cherished memories with loved ones, and savour the natural beauty that surrounds us.</p>
  </section>
</main>
</body>
</html>
```